Cercle doré
Zielgruppe
Branche: klassische Musik; Musikgruppe: Klaviertrio (Geige, Cello, Klavier) Gesucht wird ein Flyer, den wir zur Aussendarstellung nutzen können. Zielgruppe sind Veranstalter von klassisch-konservativen Konzerten. Inhalt: Fotos der 3 MusikerInnen, 3x Porträtfoto, 1 Gesamtfoto, 3 Biografien, 1 Text zu unserem Klaviertrio. Der Flyer soll hauptsächlich per mail versandt werden, eine geringe Stückzahl soll ausgedruckt werden.
Format: DIN lang105 QUER !! 210 x 105 mm Vorder- und Rückseite ODER:
DIN lang 105 quer Einbruchfalz
Aufgabenstellung
Das Klaviertrio heisst "Cercle doré", wir spielen hauptsächlich klassisch-romantische Werke. Das Design sollte klassisch-romantisch, aber nicht zu verschnörkelt sein.

```html
<!DOCTYPE html>
<html lang="de">
<head>
<meta charset="utf-8">
<title>Cercle doré – Flyer</title>
<link href="https://fonts.googleapis.com/css2?family=Noto+Serif:ital,wght@0,400;1,400&display=swap" rel="stylesheet">
<style>
  :root{
    --page:#f2f2f2;
    --ink:#2a2a2a;
    --silver-light:#f7f7f7;
    --silver:#dcdcdc;
    --silver-dark:#bdbdbd;
    --footer:#d8d8d8;
    --rule:#8a8a8a;
  }
  *{margin:0;padding:0;box-sizing:border-box}
  html,body{width:1200px;height:1200px;overflow:hidden}
  body{background:var(--page);font-family:"Noto Serif",Georgia,serif;color:var(--ink);position:relative}

  .flyer{position:absolute;left:214px;width:791px;height:396px;box-shadow:0 3px 8px rgba(0,0,0,.25);overflow:hidden}
  .flyer--front{top:220px;background:radial-gradient(ellipse at 30% 60%,var(--silver-light),var(--silver) 70%,var(--silver-dark))}
  .flyer--back{top:640px;background:#fff}

  .front__photo{position:absolute;left:300px;top:0;width:491px;height:396px;background:linear-gradient(100deg,rgba(220,220,220,0) 0%,rgba(220,220,220,0) 8%,#c99a4a 24%,#6b3a2e 44%,#2a2428 60%,#1f5a55 80%,#1c4f4c 100%)}
  .front__head{position:absolute;left:0;top:0;width:480px;height:93px;background:linear-gradient(90deg,#fbfbfb 0%,#f0f0f0 75%,rgba(240,240,240,0) 100%)}
  .front__title{position:absolute;left:16px;top:4px;font-size:50px;font-weight:400;color:#222;white-space:nowrap}
  .front__instruments{position:absolute;left:19px;top:58px;font-size:24px;color:#333;white-space:nowrap}
  .front__quote{position:absolute;left:24px;top:140px;font-style:italic;font-size:24px;line-height:30px;color:#2a2a2a;white-space:nowrap}
  .front__author{position:absolute;left:150px;top:211px;font-style:italic;font-size:15px;color:#333}
  .front__intro{position:absolute;left:24px;top:262px;width:300px;font-size:14px;line-height:17.6px;color:#1e1e1e}

  .back__portrait{position:absolute;top:0;height:362px}
  .back__portrait--violin{left:0;width:264px;background:linear-gradient(180deg,#e8e6ee 0%,#d8c08a 40%,#e9e4e6 100%)}
  .back__portrait--cello{left:264px;width:263px;background:linear-gradient(180deg,#e4e4e4 0%,#8a4a34 35%,#2d5450 70%,#e6e6e6 100%)}
  .back__portrait--piano{left:527px;width:264px;background:linear-gradient(180deg,#f1f1f1 0%,#6b4a3a 30%,#2b2e36 60%,#e8e8e8 100%)}

  .bio{position:absolute;top:140px;height:222px;background:rgba(255,255,255,.86);padding:8px 0 0 20px}
  .bio--violin{left:8px;width:242px}
  .bio--cello{left:277px;width:237px}
  .bio--piano{left:539px;width:242px}
  .bio__name{font-size:15px;font-weight:400;color:#222;padding-bottom:4px;border-bottom:1px solid var(--rule);width:calc(100% - 14px);margin-bottom:8px;white-space:nowrap}
  .bio__text{font-size:9.4px;line-height:10.8px;color:#2a2a2a;width:calc(100% - 18px)}

  .back__contact{position:absolute;left:0;top:362px;width:100%;height:34px;background:var(--footer);font-size:17px;color:#2a2a2a;text-align:center;line-height:34px;white-space:nowrap}
</style>
</head>
<body>

<section class="flyer flyer--front">
  <div class="front__photo" role="img" aria-label="Gruppenfoto des Trios: Geigerin mit Violine, Cellist mit Cello, Pianistin im grünen Kleid"></div>
  <div class="front__head"></div>
  <h1 class="front__title">Cercle doré</h1>
  <p class="front__instruments">Geige | Cello |Klavier</p>
  <p class="front__quote">„Musik ist der Raum<br>zwischen den Noten“</p>
  <p class="front__author">Claude Delorme</p>
  <p class="front__intro">Das Klaviertrio „Cercle doré“ spielt die berühmtesten Werke aus der Romantik wie Lenzfeld, Hartwig-Brennecke, Sokolinov, Valmorin und Dvoranski. Die Resonanz des Publikums:genussvoll begeistert!</p>
</section>

<section class="flyer flyer--back">
  <div class="back__portrait back__portrait--violin" role="img" aria-label="Porträtfoto der Geigerin"></div>
  <div class="back__portrait back__portrait--cello" role="img" aria-label="Porträtfoto der Cellistin mit Cello"></div>
  <div class="back__portrait back__portrait--piano" role="img" aria-label="Porträtfoto des Pianisten"></div>

  <article class="bio bio--violin">
    <h2 class="bio__name">Ilona Varga, Violine</h2>
    <p class="bio__text">Die ungarische Geigerin Ilona Varga hat sich als äußerst vielseitige Musikerin einen Namen gemacht: sie arbeitet als Solistin, Konzertmeisterin und Kammermusikerin und gründete darüber hinaus verschiedene erfolgreiche Ensembles. Ihr solistisches Repertoire reicht von den klassischen Violinkonzerten und virtuosen Meisterstücken bis hin zu modernen Kompositionen. Ihre Experimentierfreude ist über Deutschlands Grenzen hinaus bekannt; zeitgenössische europäische Komponisten arbeiten gerne mit ihr zusammen um neue Klangfarben und Klangfarben zu entwickeln.</p>
  </article>

  <article class="bio bio--cello">
    <h2 class="bio__name">Marie-Luise Brandt, Cello</h2>
    <p class="bio__text">Marie-Luise Brandt wurde in München geboren und spezialisierte sich bereits während ihres Studiums in Würzburg, Nürnberg und Düsseldorf auf die Kammermusik. Ihr intensives Streichquartett-Studium vervollständigte sie beim legendären Aurora Quartett in Stuttgart. Nach zahlreichen Wettbewerbserfolgen und Auszeichnungen widmete sie sich verstärkt zeitgenössischer Musik und der Uraufführung ihr gewidmeter Werke. Marie-Luise Brandt arbeitete lange Zeit am Rheinbühne Theater in Essen und gilt seitdem auch als viel gefragte Cellistin und Studiomusikerin für Rock- und Pop-Produktionen.</p>
  </article>

  <article class="bio bio--piano">
    <h2 class="bio__name">Gábor Halmi, Klavier</h2>
    <p class="bio__text">Der Pianist Gábor Halmi ist ebenfalls Ungar und langjähriger Kammermusikpartner von Ilona Varga. Er studierte in Budapest an der Donau-Musikakademie in Budapest und arbeitete anschliessend als Dozent am Pannonia-Konservatorium. Seit 1990 lebt und arbeitet Gábor Halmi als Solist und begehrter Begleiter in Deutschland. 1999 gründete der Pianist die Musikschule Halmi in Wesseling und etablierte sich in den folgenden Jahren nicht nur als Pianist sondern auch als erfolgreicher Klavierpädagoge.</p>
  </article>

  <p class="back__contact">Kontakt: Marie-Luise Brandt | mobil +49 170 5538 214 | mail ml.brandt@notenraum.de</p>
</section>

</body>
</html>
```